Yoga/movement guide/teacher for adult yoga practice and kid yoga

What is the positioning or mission statement of your company? to guide individuals in a yoga-based safe and sustainable movement practice applicable to all ages and body types. Currently my focus is working with children in daycare and school settings, but my goal is to expand into private yoga practice for adults, and potentially as part of rented space in studios. I hope to find a way to work with children AND adults (so would love for logo to be appealing to both), but current focus is with children based on need and demand in the community. yoga for children also compliments my backround as a pediatrician/neonatologist, and I greatly miss interacting with children. I also want to emphasize a yoga/movement practice that is focused more on what one feels internally through movement. NOT what one looks like asthetically. I believe in removing all mirrors from yoga/movement practice. It should be an experience of movement/poses/yoga through appropriate cueing and education. It is not about the details of how far the knee should bend, or how high the leg should be. Focusing on foudation first, core, then core engagement and ultimately expression of poses/movements. A focus on strength, stability and mobility, not just flexibility, which is the common perception/association with yoga. I also want individuals to learn to be an advocate of their own health. Through guidance, I hope for individuals to connect with their body so they know themselves so well to be able to advocate for themselves in the modern healthcare world. This internal experience and connection is so essential in a world where modern medicine has become a business and it is all about making a dollar. the connection with patients is lost, and individuals need to learn to empower themselves and through their new found voice to be able to articulate what is wrong.<br/>Does your company have a tagline or slogan that should be included with the logo? "Practice Radiant Movement"<br/>What do you hope your company can be known for? Accessible yoga for a sustained practice. A guided movement practice where one gains information and knowledge of oneself through a mind/body connection. For one feel good physically with a new awaraness of their internal radiance that exists in all beings. Physical rejuvenation egnites a light and increases energy to flow through the physical body, which ultimately tranlates into works of kindness for others and out in the world. <br/>What color palettes might you prefer? why? love the colors currently chosen<br/>Where will the logo be primarily used? initially business cards, but hopefully future websites, t-shirts, and potentially local magazine adds. Also starting with a small couple of banners for community events in the area. I currently practice as a nomad out of my car :)<br/>Are there any elements you would prefer to see in the logo? Movement. A modern depiction of a human body/figure practicing movement. Hoping to avoid a stereotypical yoga pose per say, just because I want to people to think of it more of a movement practice with yoga roots. Modern yoga. There are elements of breathing and connecting with oneself through the flow of breath and movement, but I do not focus on the meditative/cerebral aspect of the yoga practice. What I teach is almost reaching a meditative state through movement. I personally don't practice, nor resonate with just seated meditation. just not my thing :)<br/>In your opinion, what defines a well-designed logo? curiosity. enough info for individuals to think they know what it means, but want to know more. invokes curiosity, but not too abstract. Reproducible. not too complicated. I want also to invoke a community feel, so a design that appeals to all people within a community. <br/>What is your preference in reference to icons, typography, spokespeople (characters), etc.? modern design. I love the idea of a logo for my purposes, to invoke a sense of movement from within. So not too static. <br/>What words or icons must be included in the logo? movement with yoga roots. <br/>What logos do you like and why? A representation, but not exact. I think some ambiguity is intriguing for others, and also memorable. I want it to be an artistic representation of movement/yoga<br/>What logos do you dislike and why? too busy, too loud. <br/>In your opinion, what is the primary purpose for a logo? association<br/>Who is the primary target audience? (who is most likely to use your services/product?) Children and their parents, but ultimately to expand into teaching adults. I even have aspirations of prenatal and post-natal yoga. Potentially incorporating infants. <br/>Who currently uses your product the most? n/a (working in schools/daycare currently. It is currently all volunteer)<br/>Are you pleased with the range of people your company serves? n/a<br/>Are you looking to expand, modify, or completely change your target audience? or will it remain the same? yes! expand into an adult audience. <br/>How do you plan to focus on your target audience? currently by working through schools and daycares. hopefully ultimately through after school care programs and then offering kid yoga in an existing yoga studio (working on this with Quillbrook in Ridgeland, currently)<br/>What are your main forms of advertising? word of mouth, schools, daycares. Happy kids talking to their parents about the yoga class they took and happy teachers :)<br/>How do most customers find out about your company?<br/>Which gender are you targeting? All genders! However, with kid yoga, often the maternal individual in the child's life is more involved with decision making as far as extracurricular activities

Target Market(s)

individuals and families interested in wellness and feeling great

Contact Information for Business Card

Dana Whitford
Yoga Instructor
RYT-200, RCYT

certified yoga teacher for adults and children

Colors

Requirements
Must have
• "Practice Radiant Movement"
Nice to have
• logo with same colors

```html
<!DOCTYPE html>
<html lang="en">
<head>
<meta charset="utf-8">
<title>Glowpath Studio – Business Card</title>
<link href="https://fonts.googleapis.com/css2?family=Amatic+SC:wght@400;700&family=Patrick+Hand&display=swap" rel="stylesheet">
<style>
  :root {
    --backdrop: #2a2a2c;
    --paper: #ffffff;
    --sun: #f5d83f;
    --sun-soft: #fbeea0;
    --teal: #7cc8d2;
    --ink: #6b6b6b;
  }
  * { box-sizing: border-box; margin: 0; padding: 0; }
  html, body { width: 1200px; height: 901px; overflow: hidden; }
  body {
    background: var(--backdrop);
    display: flex;
    flex-direction: column;
    align-items: center;
    justify-content: center;
    gap: 34px;
    font-family: "Patrick Hand", cursive;
  }
  .card {
    position: relative;
    width: 700px;
    height: 400px;
    background: var(--paper);
    overflow: hidden;
    box-shadow: 0 10px 24px rgba(0,0,0,.45);
  }
  /* front */
  .card-front .wash { position: absolute; inset: 0; }
  .brand {
    position: absolute;
    display: flex;
    align-items: center;
    gap: 14px;
  }
  .brand-dot {
    border-radius: 50%;
    background: var(--sun);
    flex-shrink: 0;
  }
  .brand-name {
    font-family: "Patrick Hand", cursive;
    color: var(--ink);
    line-height: 1;
    white-space: nowrap;
  }
  .card-front .brand { left: 190px; top: 152px; }
  .card-front .brand-dot { width: 96px; height: 96px; }
  .card-front .brand-name { font-size: 52px; }

  /* back */
  .band {
    position: absolute; left: 0; width: 100%;
    background: var(--teal);
  }
  .band-top { top: 0; height: 36px; }
  .band-bottom { bottom: 0; height: 92px; }
  .card-back .brand { left: 60px; top: 139px; }
  .card-back .brand-dot { width: 62px; height: 62px; }
  .card-back .brand-name { font-size: 32px; }

  .holder {
    position: absolute;
    left: 400px; top: 70px; width: 300px;
    border-bottom: 2px solid var(--teal);
    padding-bottom: 4px;
    font-family: "Amatic SC", cursive;
    font-weight: 700;
    font-size: 72px;
    line-height: 1;
  }
  .holder .first { color: var(--sun); }
  .holder .last { color: var(--teal); }

  .contacts {
    position: absolute;
    left: 460px; top: 186px;
    list-style: none;
  }
  .contacts li {
    display: flex;
    align-items: center;
    gap: 16px;
    font-size: 22px;
    color: var(--ink);
    height: 28px;
  }
  .contacts svg { width: 18px; height: 18px; fill: var(--teal); }
</style>
</head>
<body>

  <section class="card card-front" aria-label="Card front">
    <svg class="wash" viewBox="0 0 700 400" preserveAspectRatio="none" role="img" aria-label="Yellow brush-stroke wash framing the card">
      <defs>
        <linearGradient id="leftWash" x1="0" y1="0" x2="1" y2="0">
          <stop offset="0" stop-color="var(--sun)"/>
          <stop offset="1" stop-color="var(--sun-soft)"/>
        </linearGradient>
        <linearGradient id="rightWash" x1="1" y1="0" x2="0" y2="0">
          <stop offset="0" stop-color="var(--sun)"/>
          <stop offset="1" stop-color="var(--sun-soft)"/>
        </linearGradient>
      </defs>
      <path d="M0 0 H170 C120 120 130 260 200 400 H0 Z" fill="url(#leftWash)"/>
      <path d="M700 0 V400 H600 C580 300 630 160 590 40 L610 0 Z" fill="url(#rightWash)"/>
    </svg>
    <div class="brand">
      <span class="brand-dot"></span>
      <span class="brand-name">Glowpath Studio</span>
    </div>
  </section>

  <section class="card card-back" aria-label="Card back">
    <div class="band band-top"></div>
    <div class="band band-bottom"></div>

    <div class="brand">
      <span class="brand-dot"></span>
      <span class="brand-name">Glowpath Studio</span>
    </div>

    <h1 class="holder"><span class="first">Full</span> <span class="last">Name</span></h1>

    <ul class="contacts">
      <li>
        <svg viewBox="0 0 24 24" aria-hidden="true"><path d="M6.6 10.8c1.4 2.8 3.8 5.1 6.6 6.6l2.2-2.2c.3-.3.7-.4 1-.2 1.1.4 2.3.6 3.6.6.6 0 1 .4 1 1V20c0 .6-.4 1-1 1C10.6 21 3 13.4 3 4c0-.6.4-1 1-1h3.5c.6 0 1 .4 1 1 0 1.3.2 2.5.6 3.6.1.3 0 .7-.2 1z"/></svg>
        Phone Number
      </li>
      <li>
        <svg viewBox="0 0 24 24" aria-hidden="true"><path d="M2 5h20v14H2z M3.5 6.5 12 13l8.5-6.5" stroke="#fff" stroke-width="1.5"/></svg>
        E-mail
      </li>
      <li>
        <svg viewBox="0 0 24 24" aria-hidden="true"><path d="M12 2a7 7 0 0 0-7 7c0 5 7 13 7 13s7-8 7-13a7 7 0 0 0-7-7zm0 9.5A2.5 2.5 0 1 1 12 6.5a2.5 2.5 0 0 1 0 5z"/></svg>
        Adresse
      </li>
      <li>
        <svg viewBox="0 0 24 24" aria-hidden="true"><circle cx="12" cy="12" r="10"/><path d="M2 12h20M12 2c3 3 3 17 0 20M12 2c-3 3-3 17 0 20" stroke="#fff" stroke-width="1.3" fill="none"/></svg>
        Website
      </li>
    </ul>
  </section>

</body>
</html>
```